Mortgage Company needs some fresh looking business cards to replace current outdated design

Looking for fresh ideas. The only requirement is that the card must show the following:Keystead Logo (uploaded)Keystead slogan "loans made plain"Fair Dwelling Creditor logo (uploaded)Keystead NMLS #583017 (see current bus card, uploaded)Website as shown on sampleColor Codes as follows:Green = PMS 555 , #2b7051 , CMYK 83 33 77 21Rust = PMS 471 , #bc6225 , CMYK 21 70 100 8Would like two sided card. Front will have all of the above info, and back will have just the logo.

Target Market(s)

Consumers and Real Estate Agents

Industry/Entity Type

Mortgage Lender

Contact Information for Business Card

Color Codes as follows:
Green = PMS 555 , #2b7051 , CMYK 83 33 77 21
Rust = PMS 471 , #bc6225 , CMYK 21 70 100 8

Would like two sided card. Front will have all of the above info, and back will have just the logo.

Requirements
Must have
• Keystead Logo (uploaded)
• Keystead slogan "loans made plain"
• Fair Dwelling Creditor logo (uploaded)
• Keystead NMLS #583017 (see current bus card, uploaded)
• Website as shown on sample

```html
<!DOCTYPE html>
<html lang="en">
<head>
<meta charset="utf-8">
<title>Keystead Mortgage Business Card</title>
<link href="https://fonts.googleapis.com/css2?family=Open+Sans:wght@400;600&family=Playfair+Display:ital,wght@0,400;1,400&display=swap" rel="stylesheet">
<style>
  :root {
    --green: #1f6b57;
    --rust: #c96a18;
    --white: #ffffff;
    --backdrop: #2b2e33;
    --photo-light: #d9d9d9;
    --photo-dark: #6f6a6a;
  }
  * { box-sizing: border-box; margin: 0; padding: 0; }
  html, body { width: 1200px; height: 900px; overflow: hidden; }
  body {
    background: var(--backdrop);
    font-family: "Open Sans", sans-serif;
    position: relative;
  }
  .card {
    position: absolute;
    left: 260px;
    width: 680px;
    height: 389px;
    border-radius: 22px;
    overflow: hidden;
    background: var(--white);
  }
  .card--front { top: 50px; }
  .card--back { top: 479px; }

  /* front */
  .band-green {
    position: absolute; left: 0; right: 0; top: 150px; height: 140px;
    background: var(--green);
  }
  .band-rust {
    position: absolute; left: 0; right: 0; top: 290px; bottom: 0;
    background: var(--rust);
  }
  .portrait {
    position: absolute; left: 44px; top: 40px; width: 170px; height: 140px;
    border: 4px solid var(--white);
    background: radial-gradient(circle at 50% 40%, var(--photo-light), var(--photo-dark));
  }
  .agent {
    position: absolute; left: 44px; top: 192px;
  }
  .agent__name {
    font-family: "Playfair Display", serif;
    font-size: 22px; color: var(--white); letter-spacing: 0.5px; line-height: 1.2;
  }
  .agent__title, .agent__nmls {
    font-family: "Playfair Display", serif;
    font-style: italic; font-size: 14px; color: var(--rust); line-height: 1.4;
  }
  .brand {
    position: absolute; right: 44px; top: 52px; text-align: left;
  }
  .brand__name {
    font-family: "Open Sans", sans-serif;
    font-weight: 600;
    color: var(--green); font-size: 28px; line-height: 1.1;
  }
  .brand__tagline {
    font-family: "Open Sans", sans-serif;
    font-size: 12px; letter-spacing: 2px; text-transform: uppercase;
    color: var(--rust); margin-top: 10px;
  }
  .contact {
    position: absolute; left: 400px; top: 162px; list-style: none;
    color: var(--white); font-size: 14px; line-height: 22px;
  }
  .contact li { display: flex; align-items: center; gap: 8px; }
  .contact svg { width: 14px; height: 14px; flex: none; }
  .contact .contact__plain { padding-left: 22px; }
  .apply {
    position: absolute; left: 44px; top: 308px;
    color: var(--white); font-size: 15px; line-height: 1.45;
  }
  .lender-badge {
    position: absolute; right: 40px; bottom: 24px; width: 44px; height: 44px;
    border: 3px solid var(--white); border-radius: 3px;
  }

  /* back */
  .back-brand {
    position: absolute; left: 0; right: 0; top: 140px; text-align: center;
  }
  .back-brand .brand__name { font-size: 52px; }
  .back-brand .brand__tagline { font-size: 16px; letter-spacing: 3px; margin-top: 18px; }
</style>
</head>
<body>

<section class="card card--front">
  <div class="band-green"></div>
  <div class="band-rust"></div>
  <div class="portrait" role="img" aria-label="Portrait photograph of the loan officer"></div>

  <div class="brand">
    <div class="brand__name">Keystead Mortgage</div>
    <div class="brand__tagline">loans made plain</div>
  </div>

  <div class="agent">
    <div class="agent__name">DALE BRENNICK</div>
    <div class="agent__title">Job Title</div>
    <div class="agent__nmls">NMLS #583017</div>
  </div>

  <ul class="contact">
    <li>
      <svg viewBox="0 0 14 14" aria-hidden="true"><path d="M3 1h2l1 3-1.5 1a7 7 0 0 0 4.5 4.5L10 8l3 1v2a2 2 0 0 1-2 2A11 11 0 0 1 1 3a2 2 0 0 1 2-2z" fill="var(--rust)"/></svg>
      000 000 0000
    </li>
    <li>
      <svg viewBox="0 0 14 14" aria-hidden="true"><rect x="3.5" y="0.5" width="7" height="13" rx="1.5" fill="none" stroke="var(--rust)" stroke-width="1.4"/><circle cx="7" cy="11" r="0.9" fill="var(--rust)"/></svg>
      000 000 0000
    </li>
    <li>
      <svg viewBox="0 0 14 14" aria-hidden="true"><rect x="0.5" y="2.5" width="13" height="9" fill="var(--rust)"/><path d="M1 3l6 5 6-5" fill="none" stroke="var(--green)" stroke-width="1.2"/></svg>
      youremail@keystead.com
    </li>
    <li class="contact__plain">2180 Larkspur Ave Ste 310</li>
    <li class="contact__plain">Fairview, TX 75069</li>
  </ul>

  <div class="apply">
    Apply online at:<br>
    www.keystead.com
  </div>

  <div class="lender-badge" role="img" aria-label="Fair Dwelling Creditor badge"></div>
</section>

<section class="card card--back">
  <div class="back-brand">
    <div class="brand__name">Keystead Mortgage</div>
    <div class="brand__tagline">loans made plain</div>
  </div>
</section>

</body>
</html>
```